Letterhead to Prospective Clients

Create a letterhead (word & canva) that I will use to send letters to prospective clients and also include the Coralwood Estate Partners Logo, My Contact Details and Interchangeable "Suburb". Use the same font and colour pallete

Maris Dulworth | "Suburb" Specialist - Redlands & Surrounds
Mobile: 0417 862 095
Email: MD@CoralwoodEstatePartners.com.au

```html
<!DOCTYPE html>
<html lang="en">
<head>
<meta charset="utf-8">
<title>Coralwood Estate Partners – Letterhead</title>
<link href="https://fonts.googleapis.com/css2?family=Arimo:wght@400;700&family=Montserrat:wght@400;500;700&display=swap" rel="stylesheet">
<style>
  :root {
    --navy: #0b1a3b;
    --tan: #d9a878;
    --ink: #1a1a1a;
    --paper: #ffffff;
  }
  * { margin: 0; padding: 0; box-sizing: border-box; }
  html, body { width: 1200px; height: 1200px; overflow: hidden; }
  body { background: var(--navy); position: relative; font-family: "Arimo", Arial, sans-serif; color: var(--ink); }
  .sheet { position: absolute; left: 207px; top: 45px; width: 785px; height: 1110px; background: var(--paper); }
  .brand { position: absolute; left: 79px; top: 44px; color: var(--navy); font-family: "Montserrat", sans-serif; font-weight: 500; line-height: 1; }
  .brand-name { font-size: 34px; letter-spacing: 3px; text-transform: uppercase; }
  .brand-sub { display: block; margin-top: 10px; font-size: 9px; letter-spacing: 3.2px; text-transform: uppercase; padding-left: 30px; }
  .contact { position: absolute; right: 80px; top: 43px; text-align: right; font-size: 13px; line-height: 22px; }
  .contact-row { display: flex; justify-content: flex-end; align-items: center; gap: 7px; }
  .contact-row svg { width: 12px; height: 12px; fill: var(--tan); }
  .rule { position: absolute; left: 80px; width: 625px; display: flex; align-items: center; }
  .rule-top { top: 146px; }
  .rule-bottom { top: 1048px; }
  .rule .tan { background: var(--tan); height: 3px; width: 168px; }
  .rule .navy { background: var(--navy); height: 2px; flex: 1; }
  .rule-bottom .navy { height: 3px; }
  .sender { position: absolute; left: 76px; top: 201px; font-weight: 700; font-size: 15px; line-height: 23px; color: #000; }
  .date { position: absolute; right: 82px; top: 201px; font-family: "Montserrat", sans-serif; font-size: 13px; }
  .recipient { position: absolute; left: 76px; top: 287px; font-size: 14px; }
  .salutation { position: absolute; left: 75px; top: 327px; font-size: 16px; }
  .body-copy { position: absolute; left: 76px; top: 371px; width: 627px; font-size: 15px; line-height: 20.8px; text-align: justify; }
  .body-copy p + p { margin-top: 21px; }
  .body-copy p.tight { margin-top: 0; }
  .signoff { position: absolute; left: 76px; top: 706px; }
  .signoff-word { font-family: "Montserrat", sans-serif; font-weight: 700; font-size: 16px; }
  .signature { margin-top: 14px; width: 158px; height: 32px; background: linear-gradient(90deg, #eef0f4, #f7f8fa); }
  .signer-name { margin-top: 6px; font-size: 15px; }
  .signer-title { margin-top: 5px; font-size: 12px; text-transform: uppercase; }
</style>
</head>
<body>
  <main class="sheet">
    <header>
      <div class="brand"><span class="brand-name">Coralwood</span><span class="brand-sub">Estate Partners</span></div>
      <div class="contact">
        <div class="contact-row">0417 862 095
          <svg viewBox="0 0 24 24" aria-hidden="true"><path d="M3 9c0-3 4-5 9-5s9 2 9 5v2h-5V9H8v2H3zM6 12h12l2 8H4z"/></svg>
        </div>
        <div class="contact-row">MD@CoralwoodEstatePartners.com.au
          <svg viewBox="0 0 24 24" aria-hidden="true"><path d="M22 2 2 11l7 3 2 8 3-6 6 4z"/></svg>
        </div>
      </div>
    </header>
    <div class="rule rule-top"><span class="tan"></span><span class="navy"></span></div>

    <div class="sender">Maris Dulworth | "Suburb" Specialist<br>Redlands &amp; Surrounds</div>
    <div class="date">25 June, 2029</div>

    <div class="recipient">To:</div>
    <div class="salutation">Dear Mr. Hallett</div>

    <section class="body-copy">
      <p>Lorem ipsum dolor sit amet, consectetur adipiscing elit, sed do eiusmod tempor incididunt ut labore et dolore magna aliqua. Eget nunc lobortis mattis aliquam faucibus purus. Tincidunt praesent semper feugiat nibh. Mi proin sed libero enim sed faucibus turpis. Tempor id eu nisl nunc mi. Suscipit adipiscing bibendum est ultricies integer. Mattis nunc sed blandit libero volutpat sed.</p>
      <p>Ac ut consequat semper viverra nam. Adipiscing bibendum est ultricies integer quis auctor elit sed vulputate. Elit ut aliquam purus sit. Morbi enim nunc faucibus a pellentesque sit amet porttitor. Sem fringilla ut morbi tincidunt augue interdum. Ac turpis egestas sed tempus urna et pharetra. Ullamcorper dignissim cras tincidunt lobortis feugiat vivamus at augue eget.</p>
      <p class="tight">Lorem ipsum dolor sit amet, consectetur adipiscing elit, sed do eiusmod tempor incididunt ut labore et dolore magna aliqua. Eget nunc lobortis mattis aliquam faucibus purus. Tincidunt praesent semper feugiat nibh. Mi proin sed libero enim sed faucibus turpis. Tempor id eu nisl nunc mi.</p>
    </section>

    <div class="signoff">
      <div class="signoff-word">Regards,</div>
      <div class="signature" role="img" aria-label="Handwritten signature of Maris Dulworth"></div>
      <div class="signer-name">Maris Dulworth</div>
      <div class="signer-title">Suburb" Specialist</div>
    </div>

    <div class="rule rule-bottom"><span class="navy"></span><span class="tan"></span></div>
  </main>
</body>
</html>
```